TOR Global (Terrain Orchard and Resources) is a company positioning itself as a global leader in regenerative and sustainable agriculture and irrigation technologies and solutions, with a focus on soil health. Please read the attached information (which can be used in the website).
We're looking for a modern website which also compliments the agricultural sector and the natural resources we work with. We want the website to be fairly concise and to the point without elaborating too much. We would rather attract the clients to engage with us rather than drawing their own conclusions from the website.

```html
<!DOCTYPE html>
<html lang="en">
<head>
<meta charset="utf-8">
<title>TOR Global – Terrain Orchard and Resources</title>
<link href="https://fonts.googleapis.com/css2?family=Outfit:wght@400;500;600&family=Raleway:wght@400;500;600;700&display=swap" rel="stylesheet">
<style>
:root{
  --cream:#f6f5ee;
  --navy:#3f5d8f;
  --navy-dark:#2f4a78;
  --ink:#1e1f1a;
  --text:#3b3b36;
  --muted:#55554f;
  --olive:#5b6a2c;
  --sage:#8a9a5b;
  --dark:#262820;
  --darker:#1b1c18;
  --white:#ffffff;
}
*{box-sizing:border-box;margin:0;padding:0}
html,body{width:1200px;height:4169px;overflow:hidden}
body{position:relative;background:var(--cream);font-family:"Raleway",sans-serif;color:var(--text)}
.abs{position:absolute}
.btn{position:absolute;display:flex;align-items:center;justify-content:center;background:var(--navy);color:var(--white);font:700 13px "Raleway",sans-serif;letter-spacing:.3px;text-transform:uppercase}
.photo{position:absolute}

/* header */
.topbar{left:632px;top:0;width:568px;height:32px;background:var(--navy-dark);clip-path:polygon(0 0,100% 0,100% 100%,32px 100%)}
.topbar span{position:absolute;top:8px;color:#fff;font-size:12.5px}
.dot{position:absolute;width:12px;height:12px;border:1.5px solid #fff;border-radius:50%}
.brand{display:flex;align-items:center;gap:10px}
.brand i{width:22px;height:22px;background:var(--navy);display:block}
.brand b{font:600 30px "Outfit",sans-serif;color:var(--navy)}
.nav a{position:absolute;top:54px;font:500 13.5px "Raleway",sans-serif;color:var(--ink);text-decoration:none;text-transform:uppercase}
.nav a.on{color:#8a8a84}

/* hero */
.hero{left:0;top:89px;width:1200px;height:622px;background:linear-gradient(180deg,#7d9a6a 0%,#4f6b34 40%,#2f4a1e 75%,#3b3424 100%)}
.hero-sub{left:66px;top:282px;font:500 27px "Outfit",sans-serif;color:#fff}
.hero-title{left:66px;top:316px;font:500 50px/58px "Outfit",sans-serif;color:#fff}

/* about */
.eyebrow{font:500 14px "Raleway",sans-serif;color:var(--ink);text-transform:uppercase}
.section-title{font:500 45px/53px "Outfit",sans-serif;color:var(--ink)}
.body-copy{font:400 15.5px/27px "Raleway",sans-serif;color:var(--text)}

/* products */
.service-card{position:absolute;top:1789px;width:333px;height:338px;background:#fff;border-radius:4px;box-shadow:0 3px 14px rgba(0,0,0,.08);text-align:center}
.service-card .icon{position:absolute;left:124px;top:-43px;width:86px;height:86px;border-radius:50%;background:#fff;box-shadow:0 2px 8px rgba(0,0,0,.12);display:flex;align-items:center;justify-content:center}
.service-card h3{margin-top:70px;font:500 22px/30px "Outfit",sans-serif;color:var(--ink)}
.service-card p{margin:18px auto 0;width:295px;font:400 13px/22px "Raleway",sans-serif;color:var(--muted)}
.service-card .btn{left:95px;bottom:36px;width:143px;height:46px}
.chev{position:absolute;font:400 22px "Raleway",sans-serif;color:var(--ink)}

/* why */
.why-card{position:absolute;top:2325px;width:345px;height:375px;background:#efeee6;border-radius:4px}
.why-card h3{position:absolute;left:13px;top:20px;font:500 22px/29px "Outfit",sans-serif;color:var(--ink)}
.why-card .photo{left:0;top:90px;width:345px;height:190px}
.why-card p{position:absolute;left:13px;top:295px;width:315px;font:400 13.5px/22px "Raleway",sans-serif;color:var(--muted)}

/* impact */
.impact-band{left:0;top:2812px;width:1200px;height:1357px;background:var(--dark)}
.contact-panel{left:66px;top:3420px;width:1067px;height:460px;background:var(--olive);border-radius:14px;clip-path:polygon(0 0,560px 0,640px 80px,100% 80px,100% 100%,0 100%)}
.field{position:absolute;border:1px solid rgba(255,255,255,.35);color:rgba(255,255,255,.75);font:400 12px "Raleway",sans-serif;padding:14px 12px}

/* footer */
.footer-box{left:98px;top:3848px;width:1005px;height:330px;background:var(--darker);border-radius:26px 26px 0 0}
.foot-h{font:500 18px "Outfit",sans-serif;color:var(--sage)}
.foot-link{font:400 13.5px "Raleway",sans-serif;color:#e6e6e0}
.ring{position:absolute;width:36px;height:36px;border-radius:50%;border:1px solid rgba(255,255,255,.35);display:flex;align-items:center;justify-content:center}
.ring::after{content:"";width:12px;height:12px;border-radius:50%;background:#fff}
.c-icon{position:absolute;width:34px;height:34px;border-radius:50%;background:#3a3b35;display:flex;align-items:center;justify-content:center}
</style>
</head>
<body>

<!-- header -->
<div class="abs topbar">
  <svg class="abs" style="left:56px;top:10px" width="14" height="11" viewBox="0 0 14 11"><rect x=".75" y=".75" width="12.5" height="9.5" fill="none" stroke="#fff" stroke-width="1.3"/><path d="M1 1l6 5 6-5" fill="none" stroke="#fff" stroke-width="1.3"/></svg>
  <span style="left:78px">hello@torglobal.example</span>
  <svg class="abs" style="left:252px;top:9px" width="12" height="12" viewBox="0 0 24 24"><path d="M6.6 10.8a15 15 0 006.6 6.6l2.2-2.2c.3-.3.7-.4 1-.2 1.1.4 2.3.6 3.6.6.6 0 1 .4 1 1V20c0 .6-.4 1-1 1A17 17 0 013 4c0-.6.4-1 1-1h3.5c.6 0 1 .4 1 1 0 1.3.2 2.5.6 3.6.1.3 0 .7-.2 1z" fill="#fff"/></svg>
  <span style="left:272px">(010) 4400-7310</span>
  <div class="dot" style="left:418px;top:10px"></div>
  <div class="dot" style="left:450px;top:10px"></div>
  <div class="dot" style="left:484px;top:10px"></div>
</div>
<a class="abs brand" style="left:66px;top:30px;text-decoration:none"><i></i><b>TOR Global</b></a>
<nav class="nav">
  <a class="on" style="left:545px">Home</a>
  <a style="left:632px">About Us</a>
  <a style="left:750px">Prodcut &amp; Services</a>
  <a style="left:948px">Impact</a>
  <a style="left:1045px">Contact Us</a>
</nav>

<!-- hero -->
<section class="abs hero" role="img" aria-label="Sprinklers irrigating long green crop rows at sunset"></section>
<div class="abs hero-sub">Revolutionizing</div>
<h1 class="abs hero-title">Agriculture with<br>Regenerative Solutions</h1>
<a class="btn" style="left:66px;top:468px;width:161px;height:44px">Explore More</a>

<!-- about -->
<div class="photo" style="left:66px;top:818px;width:467px;height:486px;border-radius:10px;background:linear-gradient(180deg,#9cc0d8 0%,#c9c7a8 35%,#4e7a2e 60%,#2e4f1c 100%)" role="img" aria-label="Farmer tending young crops in a field"></div>
<div class="abs eyebrow" style="left:605px;top:862px">Welcome to</div>
<h2 class="abs section-title" style="left:605px;top:884px">Terrain Orchard<br>and Resources</h2>
<p class="abs body-copy" style="left:605px;top:1016px;width:530px">At TOR, we are committed to reshaping the future of farming through regenerative agriculture. Our solutions go beyond sustainability, actively restoring ecosystems and improving soil health while delivering superior yields. With water-efficient irrigation, innovative agronomy, and a deep focus on soil vitality, we empower farmers to grow more sustainably and profitably.</p>
<a class="btn" style="left:605px;top:1214px;width:144px;height:45px">Our Mission</a>

<!-- products -->
<div class="photo" style="left:66px;top:1412px;width:1067px;height:503px;border-radius:18px;background:linear-gradient(180deg,#4f6c2f 0%,#2f4a1d 45%,#1f3414 100%);clip-path:polygon(0 0,500px 0,580px 148px,100% 148px,100% 100%,0 100%)" role="img" aria-label="Centre-pivot irrigation spraying a green field"></div>
<div class="photo" style="left:640px;top:1375px;width:380px;height:500px;border-radius:180px 180px 0 0;background:linear-gradient(180deg,#c9a877 0%,#d9b79a 30%,#c77d5a 55%,#6a9a3a 75%,#2f4a78 100%)" role="img" aria-label="Smiling farmer carrying an armful of fresh vegetables"></div>
<h2 class="abs" style="left:98px;top:1505px;font:500 45px/54px 'Outfit',sans-serif;color:#fff">Our Core<br>Products and Services</h2>

<div class="service-card" style="left:78px">
  <div class="icon"><svg width="40" height="40" viewBox="0 0 40 40" fill="none" stroke="#222" stroke-width="1.6"><path d="M4 28h8l8 3h10l6-4M12 28v-4h6l6 3M20 18v-8M20 10c0-4 4-6 8-6 0 4-4 6-8 6zM20 12c0-3-3-5-6-5 0 3 3 5 6 5z"/></svg></div>
  <h3>Regenerative<br>Agricultural Technologies</h3>
  <p>Unlock the future of farming with the latest practices and tools designed to rebuild ecosystems, improve biodiversity, and restore soil carbon levels.</p>
  <a class="btn">Read More</a>
</div>
<div class="service-card" style="left:434px">
  <div class="icon"><svg width="40" height="40" viewBox="0 0 40 40" fill="none" stroke="#222" stroke-width="1.6"><rect x="12" y="14" width="16" height="8" rx="2"/><path d="M4 10h12M24 10h12M10 10v4M30 10v4M20 22v4M16 30l-2 4M24 30l2 4M20 30v5"/></svg></div>
  <h3>Mobile<br>Drip Irrigation (MDI)</h3>
  <p>Our advanced irrigation system maximizes water use efficiency, reduces waste, and promotes healthier crops.</p>
  <a class="btn">Read More</a>
</div>
<div class="service-card" style="left:789px">
  <div class="icon"><svg width="40" height="40" viewBox="0 0 40 40" fill="none" stroke="#222" stroke-width="1.6"><rect x="10" y="6" width="20" height="28" rx="2"/><rect x="15" y="3" width="10" height="6" rx="1"/><path d="M20 30V16M20 20c-4 0-5-3-5-5 3 0 5 2 5 5zM20 24c4 0 5-3 5-5-3 0-5 2-5 5z"/></svg></div>
  <h3 style="padding-top:15px">Agronomy Services</h3>
  <p style="margin-top:33px">Unlock the future of farming with the latest practices and tools designed to rebuild ecosystems, improve biodiversity, and restore soil carbon levels.</p>
  <a class="btn">Read More</a>
</div>
<div class="chev" style="left:28px;top:1944px">‹</div>
<div class="chev" style="left:1160px;top:1944px">›</div>

<!-- why -->
<h2 class="abs section-title" style="left:0;top:2225px;width:1200px;text-align:center">Why Choose TOR?</h2>
<div class="why-card" style="left:66px">
  <h3>Champions of<br>Regenerative Agriculture</h3>
  <div class="photo" style="background:linear-gradient(135deg,#3f6b25,#b8402c 55%,#5e8a34)" role="img" aria-label="Farmer harvesting ripe tomatoes into a crate"></div>
  <p>We don't just sustain—we regenerate, creating long-term benefits for the environment and your farm.</p>
</div>
<div class="why-card" style="left:427px">
  <h3>Cutting<br>Edge Innovation</h3>
  <div class="photo" style="background:linear-gradient(180deg,#e6e9ea 0%,#c8d6c0 45%,#6f9a3c 100%)" role="img" aria-label="Researchers reviewing crops inside a greenhouse"></div>
  <p>Access the latest technologies that promote ecosystem restoration and climate resilience.</p>
</div>
<div class="why-card" style="left:788px">
  <h3>Global Expertise</h3>
  <div class="photo" style="background:linear-gradient(180deg,#b9c4c8 0%,#5f8a6a 45%,#4a6a2c 100%)" role="img" aria-label="Two growers potting seedlings at a nursery bench"></div>
  <p>Decades of experience bringing sustainable solutions to diverse farming environments worldwide.</p>
</div>
<div class="chev" style="left:28px;top:2500px">‹</div>
<div class="chev" style="left:1160px;top:2500px">›</div>

<!-- impact -->
<section class="abs impact-band"></section>
<div class="photo" style="left:66px;top:2875px;width:540px;height:473px;border-radius:6px;background:linear-gradient(180deg,#7a8a5e 0%,#3fb3a8 35%,#6b4a32 65%,#3a2a1e 100%)" role="img" aria-label="Gardener planting seedlings into a tray of soil"></div>
<div class="photo" style="left:250px;top:2755px;width:190px;height:130px;border-radius:95px 95px 0 0;background:linear-gradient(180deg,#b99a6a,#d8b896)" role="img" aria-label="Gardener's head and shoulders above the frame"></div>
<h2 class="abs" style="left:672px;top:2958px;font:500 45px 'Outfit',sans-serif;color:#fff">Our Impact</h2>
<p class="abs" style="left:672px;top:3038px;width:470px;font:400 16px/26px 'Raleway',sans-serif;color:#e8e8e2">We are proud to help farmers build resilient farms, sequester carbon, and regenerate the land. Our approach ensures healthy soils, vibrant ecosystems, and productive crops for generations to come.</p>
<a class="btn" style="left:672px;top:3170px;width:143px;height:44px">Contact Us</a>

<!-- contact -->
<div class="abs contact-panel"></div>
<div class="photo" style="left:640px;top:3365px;width:460px;height:495px;border-radius:120px 120px 0 0;background:linear-gradient(180deg,#c9a58a 0%,#3d5f8a 40%,#b23a30 75%,#d9a877 100%)" role="img" aria-label="Smiling farmer holding a crate of fresh strawberries"></div>
<h2 class="abs" style="left:103px;top:3468px;font:500 45px 'Outfit',sans-serif;color:#fff">Get In Touch</h2>
<p class="abs" style="left:103px;top:3532px;font:400 15px 'Raleway',sans-serif;color:#f0f0ea">Duis aute irure dolor in reprehenderit in voluptate velit...</p>
<div class="field" style="left:103px;top:3587px;width:237px;height:43px">Name:</div>
<div class="field" style="left:353px;top:3587px;width:237px;height:43px">Email:</div>
<div class="field" style="left:103px;top:3645px;width:237px;height:43px">Phone:</div>
<div class="field" style="left:353px;top:3645px;width:237px;height:115px">Message:</div>
<a class="btn" style="left:103px;top:3703px;width:237px;height:43px;font-size:12px">Send</a>

<!-- footer -->
<footer class="abs footer-box">
  <div class="abs brand" style="left:35px;top:60px"><i style="background:#fff"></i><b style="color:#fff">TOR Global</b></div>
  <p class="abs" style="left:35px;top:132px;width:330px;font:400 13.5px/22px 'Raleway',sans-serif;color:#e6e6e0">At TOR, we are committed to reshaping the future of farming through regenerative agriculture.</p>
  <div class="ring" style="left:35px;top:197px"></div>
  <div class="ring" style="left:90px;top:197px"></div>
  <div class="ring" style="left:145px;top:197px"></div>

  <div class="abs foot-h" style="left:460px;top:28px">Quick Links</div>
  <div class="abs foot-link" style="left:460px;top:72px">Home</div>
  <div class="abs foot-link" style="left:460px;top:104px">About Us</div>
  <div class="abs foot-link" style="left:460px;top:136px">Prodcut &amp; Services</div>
  <div class="abs foot-link" style="left:460px;top:168px">Impact</div>
  <div class="abs foot-link" style="left:460px;top:200px">Contact Us</div>

  <div class="abs foot-h" style="left:728px;top:28px">Contact Us</div>
  <div class="c-icon" style="left:728px;top:75px"><svg width="14" height="14" viewBox="0 0 24 24"><path d="M12 2a7 7 0 00-7 7c0 5 7 13 7 13s7-8 7-13a7 7 0 00-7-7zm0 9.5A2.5 2.5 0 1112 6.5a2.5 2.5 0 010 5z" fill="#fff"/></svg></div>
  <div class="abs foot-link" style="left:772px;top:72px;line-height:22px">14 Meadow Lane<br>Fernbrook K2R 0A1</div>
  <div class="c-icon" style="left:728px;top:150px"><svg width="14" height="14" viewBox="0 0 24 24"><path d="M6.6 10.8a15 15 0 006.6 6.6l2.2-2.2c.3-.3.7-.4 1-.2 1.1.4 2.3.6 3.6.6.6 0 1 .4 1 1V20c0 .6-.4 1-1 1A17 17 0 013 4c0-.6.4-1 1-1h3.5c.6 0 1 .4 1 1 0 1.3.2 2.5.6 3.6.1.3 0 .7-.2 1z" fill="#fff"/></svg></div>
  <div class="abs foot-link" style="left:772px;top:158px">+1 (010) 555 0199</div>
  <div class="c-icon" style="left:728px;top:203px"><svg width="14" height="12" viewBox="0 0 14 11"><rect x=".75" y=".75" width="12.5" height="9.5" fill="none" stroke="#fff" stroke-width="1.3"/><path d="M1 1l6 5 6-5" fill="none" stroke="#fff" stroke-width="1.3"/></svg></div>
  <div class="abs foot-link" style="left:772px;top:211px">support@torglobal.example</div>

  <div class="abs" style="left:0;top:280px;width:560px;text-align:center;font:400 10px 'Raleway',sans-serif;color:#6a6a64">© <span style="color:var(--sage)">TOR GLOBAL</span> 2024. ALL RIGHTS RESERVED.</div>
</footer>

</body>
</html>
```